Grand Bridal Pastry Selling Method needs finishing touches to website.

We have a temporary website located at http://www.brivantaworks.example/qk/.
We are doing a responsive design and have created the architecture (layout). However, we need a professional makeover for the graphic elements and colors of the website. The website will be selling a sales course to mostly women who sell wedding cakes.
The photos within the posted website are for illustrative purposes. We will use our own photos after the website is redone.
We are open to changing the font styles, borders, header, and anything else as long as the layout is not changed.
Target Market(s)
75% women age 25-50 and men 30-60.
Industry/Entity Type
Architecture
Colors
Designer to choose colors to be used in the design.
Look and feel
Each slider illustrates characteristics of the customer's brand and the style your logo design should communicate.

```html
<!DOCTYPE html>
<html lang="en">
<head>
<meta charset="utf-8">
<title>Grand Bridal Pastry Selling Method</title>
<link rel="stylesheet" href="https://fonts.googleapis.com/css2?family=Open+Sans:ital,wght@0,400;0,700;1,700;1,800&family=Varela+Round&display=swap">
<style>
  :root {
    --orange: #f07428;
    --orange-dark: #e8661a;
    --button: #f39a1e;
    --green: #5cb85c;
    --ink: #1a1a1a;
    --white: #ffffff;
    --footer: #3b3b3b;
    --video: #060709;
    --badge: #9a9a9a;
  }
  * { margin: 0; padding: 0; box-sizing: border-box; }
  html, body { width: 1200px; height: 1156px; overflow: hidden; }
  body {
    position: relative;
    font-family: "Open Sans", Arial, sans-serif;
    background: #3a2c26;
  }
  .backdrop {
    position: absolute; inset: 0;
    background:
      radial-gradient(ellipse 260px 420px at 150px 700px, rgba(240,236,232,.85), rgba(240,236,232,0) 70%),
      radial-gradient(ellipse 200px 300px at 1120px 500px, rgba(225,205,200,.55), rgba(225,205,200,0) 70%),
      linear-gradient(90deg, #cfc7c0 0%, #6d5a4f 18%, #3f302a 50%, #4a3a33 80%, #8a7468 100%);
  }
  .page {
    position: absolute; left: 181px; top: 19px; width: 865px; height: 1137px;
    background: var(--white);
  }
  .abs { position: absolute; }
  .site-title {
    left: 43px; top: 69px;
    font-size: 20px; line-height: 24px; font-weight: 800; font-style: italic; color: var(--ink);
    white-space: nowrap;
  }
  .header-cake {
    left: 763px; top: 20px; width: 66px; height: 87px;
    background: linear-gradient(180deg, #f4f1e8 0%, #e7e3d6 60%, #9fb86a 100%);
    border-radius: 8px 8px 2px 2px;
  }
  .main-nav {
    left: 8px; top: 111px; width: 844px; height: 33px;
    background: var(--orange); display: flex;
    font-family: "Varela Round", Arial, sans-serif; font-size: 14px; color: var(--white);
  }
  .main-nav span {
    display: flex; align-items: center; justify-content: center;
    height: 100%; border-right: 1px solid rgba(255,255,255,.8);
  }
  .main-nav span:nth-child(1) { width: 100px; }
  .main-nav span:nth-child(2) { width: 137px; }
  .main-nav span:nth-child(3) { width: 238px; }
  .main-nav span:nth-child(4) { width: 104px; }
  .video-frame { left: 8px; top: 153px; width: 561px; height: 341px; background: var(--video); }
  .optin {
    left: 584px; top: 153px; width: 268px; height: 341px; background: var(--orange);
    color: var(--white);
  }
  .optin-heading {
    position: absolute; left: 0; top: 22px; width: 268px; text-align: center;
    font-size: 22px; font-weight: 700; font-style: italic; line-height: 30px; white-space: nowrap;
  }
  .optin-label {
    position: absolute; left: 35px; display: block;
    font-size: 16px; line-height: 20px; font-weight: 700; font-style: italic;
  }
  .optin-field { position: absolute; left: 33px; width: 195px; height: 22px; background: var(--white); border: 1px solid #d8d8d8; }
  .optin-button {
    position: absolute; left: 72px; top: 276px; width: 122px; height: 22px;
    background: var(--green); font-family: "Varela Round", Arial, sans-serif; font-size: 11px;
    display: flex; align-items: center; justify-content: center;
  }
  .optin-note { position: absolute; left: 0; width: 100%; top: 311px; text-align: center; font-size: 12px; line-height: 16px; font-weight: 700; }
  .section-band {
    left: 8px; top: 518px; width: 835px; height: 41px; background: var(--orange);
    color: var(--white); font-size: 15px; font-weight: 700; font-style: italic;
    display: flex; align-items: center; padding-left: 19px;
  }
  .card { top: 585px; width: 191px; height: 328px; }
  .card-photo { position: absolute; left: 0; top: 0; width: 191px; height: 120px; }
  .card-body {
    position: absolute; left: 0; top: 120px; width: 191px; height: 208px;
    background: var(--orange); color: var(--white); padding: 11px 10px;
    font-size: 9.5px; line-height: 12px; font-weight: 700;
  }
  .card-body em { display: block; margin-top: 7px; }
  .read-more {
    position: absolute; left: -10px; top: 276px; width: 130px; height: 28px;
    background: var(--button); color: var(--white); font-size: 12px; font-weight: 700;
    display: flex; align-items: center; justify-content: center;
  }
  .press { top: 958px; height: 42px; background: var(--badge); opacity: .7; border-radius: 3px; }
  .site-footer {
    left: 0; top: 1064px; width: 865px; height: 73px; background: var(--footer); color: var(--white);
  }
  .copyright { position: absolute; right: 33px; top: 12px; font-size: 15px; font-weight: 700; }
  .footer-nav { position: absolute; right: 35px; top: 43px; display: flex; gap: 38px; font-size: 13px; font-weight: 700; }
</style>
</head>
<body>
  <div class="backdrop" role="img" aria-label="Softly blurred photo of a white tiered wedding cake in a warm room"></div>

  <main class="page">
    <h1 class="abs site-title">Cracking The “Secret Code” That Unlocks Your Wedding Cake Sales!</h1>
    <div class="abs header-cake" role="img" aria-label="Small photo of a tiered wedding cake with green leaves"></div>

    <nav class="abs main-nav">
      <span>home</span><span>Who is Len Marsh</span><span>Why Len is sharing his secrets</span><span>Contact</span>
    </nav>

    <div class="abs video-frame" role="img" aria-label="Video player"></div>

    <form class="abs optin">
      <h2 class="optin-heading">Free Videos To Help<br>You Sell More Wedding<br>Cakes At Higher<br>Prices Inmmediately</h2>
      <label class="optin-label" style="top:163px">Name</label>
      <div class="optin-field" style="top:189px"></div>
      <label class="optin-label" style="top:215px">Email</label>
      <div class="optin-field" style="top:241px"></div>
      <div class="optin-button">get instant access</div>
      <p class="optin-note">No spam I promise</p>
    </form>

    <h3 class="abs section-band">3 Leading Edge Techniques For Convincing Brides To Choose You</h3>

    <article class="abs card" style="left:23px">
      <div class="card-photo" role="img" aria-label="Photo of a tiered white cake with red roses" style="background:linear-gradient(160deg,#efe9e6,#c9a9a3 60%,#a33a4a)"></div>
      <div class="card-body">In the fire video, discover a sales growth secret that reveals the two faces of your wedding cake business.<em>One side of your face displays your internet reality. It's how you run your business whether...</em></div>
      <div class="read-more">Read More</div>
    </article>
    <article class="abs card" style="left:232px">
      <div class="card-photo" role="img" aria-label="Photo of a white tiered cake with pink flowers" style="background:linear-gradient(160deg,#f2f0ee,#e4d8d4 60%,#d7a8b0)"></div>
      <div class="card-body">In the fire video, discover a sales growth secret that reveals the two faces of your wedding cake business.<em>One side of your face displays your internet reality. It's how you run your business whether...</em></div>
      <div class="read-more">Read More</div>
    </article>
    <article class="abs card" style="left:443px">
      <div class="card-photo" role="img" aria-label="Photo of an ornate white cake with peach flowers" style="background:linear-gradient(160deg,#b9b2ab,#ebe6e0 55%,#e3b8a6)"></div>
      <div class="card-body">In the fire video, discover a sales growth secret that reveals the two faces of your wedding cake business.<em>One side of your face displays your internet reality. It's how you run your business whether...</em></div>
      <div class="read-more">Read More</div>
    </article>
    <article class="abs card" style="left:652px">
      <div class="card-photo" role="img" aria-label="Photo of a pastry chef decorating a gold cake" style="background:linear-gradient(160deg,#f4f2ee,#d6c6a8 55%,#b48a4a)"></div>
      <div class="card-body">In the fire video, discover a sales growth secret that reveals the two faces of your wedding cake business.<em>One side of your face displays your internet reality. It's how you run your business whether...</em></div>
      <div class="read-more">Read More</div>
    </article>

    <div class="abs press" style="left:54px;width:44px"></div>
    <div class="abs press" style="left:156px;width:124px"></div>
    <div class="abs press" style="left:338px;width:42px"></div>
    <div class="abs press" style="left:477px;width:50px"></div>
    <div class="abs press" style="left:597px;width:98px"></div>
    <div class="abs press" style="left:747px;width:84px"></div>

    <footer class="abs site-footer">
      <p class="copyright">Copyright © 2014 The Frosting Atelier. Phone: 555.014.2290. All Rights Reserved.</p>
      <nav class="footer-nav"><span>Home</span><span>Who Is Len Marsh</span><span>Why Len Is Sharing His Secrets</span><span>Contact</span></nav>
    </footer>
  </main>
</body>
</html>
```